Red Pine Vector 1/2 Page Color Print Ad

This is a 1/2 page color print ad - no larger than 7-1/2 wide x 5 high. Please provide the ad as a high-res PDF file (preferred) or 300 dpi jpg file

Included in some way should be a description of the services Red Pine Vector LLC provides -
Red Pine Vector LLC is a Professional Information Technology Services Organization providing services in:
Strategy, Assessment, Project Management, Design, System Administration, Implementation, On-going Support and Cloud based Management Services

A logo will need to be incorporated and will be uploaded. Additionally the Red Pine Vector LLC [RPV] Web Address is www.redpinevector.net
This website will provide further insight into what RPV does as well as color schema/look/feel of existing creative design so this ad will stay within some consistent bounds of current marketing designs.
Updates

Thanks for all the submissions - we have seen some great designs and have guaranteed the project and look forward to making a decision by Tuesday. 

Thank you all for the designs and submissions.  We do appreciate it.  Our team will be discussing the designs today and a decision should be made today, tomorrow at the very latest.

Target Market(s)

Any Business person that relies on Technology to run their business and needs an IT staff and/or partner to understand and support the business goals

Industry/Entity Type

Marketing

Requirements
Must have
• Company Logo
Company Address
Phone number
Web address

This info incorporated in some way:

```html
<!DOCTYPE html>
<html lang="en">
<head>
<meta charset="utf-8">
<title>Red Pine Vector – Half Page Print Ad</title>
<link rel="stylesheet" href="https://fonts.googleapis.com/css2?family=Gelasio:wght@400;500&display=swap">
<style>
  :root {
    --page-bg: #e9e9e9;
    --ad-dark: #05070c;
    --ad-navy: #0b1a2e;
    --glow-blue: #2f7fc4;
    --glow-soft: #9fd4f4;
    --header-white: #ffffff;
    --band-blue: #1f6fae;
    --band-deep: #0e3f6e;
    --brand-navy: #2c4a78;
    --service-text: #ffffff;
    --contact-text: #d8e8f5;
  }
  * { box-sizing: border-box; margin: 0; padding: 0; }
  html, body {
    width: 1200px;
    height: 1200px;
    overflow: hidden;
    background: var(--page-bg);
  }
  .print-ad {
    position: absolute;
    left: 128px;
    top: 287px;
    width: 944px;
    height: 626px;
    overflow: hidden;
    background: var(--ad-dark);
  }
  .hero-visual {
    position: absolute;
    inset: 0;
    background:
      radial-gradient(ellipse 110px 80px at 68% 70%, rgba(230,210,255,0.55), transparent 75%),
      radial-gradient(ellipse 300px 170px at 74% 58%, rgba(159,212,244,0.45), transparent 72%),
      radial-gradient(ellipse 200px 120px at 52% 34%, rgba(127,196,238,0.3), transparent 75%),
      radial-gradient(ellipse 460px 300px at 66% 50%, rgba(47,127,196,0.4), transparent 78%),
      radial-gradient(ellipse 260px 260px at 94% 18%, rgba(60,70,90,0.55), transparent 75%),
      linear-gradient(120deg, var(--ad-dark) 0%, var(--ad-navy) 55%, #0a1422 100%);
  }
  .header-wave {
    position: absolute;
    left: 0;
    top: 0;
    width: 944px;
    height: 200px;
  }
  .brand-name {
    position: absolute;
    left: 28px;
    top: 26px;
    display: flex;
    align-items: center;
    gap: 12px;
    font-family: "Gelasio", Georgia, serif;
    font-weight: 400;
    font-size: 30px;
    line-height: 1;
    color: var(--brand-navy);
  }
  .brand-dot {
    width: 22px;
    height: 22px;
    border-radius: 50%;
    background: var(--brand-navy);
    flex: none;
  }
  .service-list {
    position: absolute;
    left: 20px;
    top: 182px;
    list-style: none;
    font-family: "Gelasio", Georgia, serif;
    font-weight: 500;
    font-size: 21px;
    line-height: 53.5px;
    color: var(--service-text);
  }
  .contact-block {
    position: absolute;
    right: 28px;
    bottom: 24px;
    text-align: right;
    font-family: "Gelasio", Georgia, serif;
    font-weight: 400;
    font-size: 16px;
    line-height: 24px;
    color: var(--contact-text);
  }
  .contact-block .web-address {
    font-weight: 500;
    font-size: 19px;
    color: var(--service-text);
  }
</style>
</head>
<body>
  <section class="print-ad">
    <div class="hero-visual" role="img" aria-label="Photo of a businessman's open hand holding a glowing laptop surrounded by floating technology icons, email envelopes and a world map"></div>

    <svg class="header-wave" viewBox="0 0 944 200" aria-hidden="true">
      <defs>
        <linearGradient id="bandGradient" x1="0" y1="0" x2="1" y2="0">
          <stop offset="0" stop-color="#0e3f6e"/>
          <stop offset="0.6" stop-color="#1f6fae"/>
          <stop offset="1" stop-color="#0e3f6e"/>
        </linearGradient>
      </defs>
      <path d="M0 0 H560 C470 40 380 100 250 128 C160 146 70 148 0 144 Z" fill="#ffffff"/>
      <path d="M0 144 C70 148 160 146 250 128 C380 100 470 40 560 0 H586 C490 48 390 112 260 140 C160 160 70 162 0 160 Z" fill="url(#bandGradient)"/>
    </svg>

    <div class="brand-name"><span class="brand-dot"></span>Red Pine Vector</div>

    <ul class="service-list">
      <li>Strategy,</li>
      <li>Assessment,</li>
      <li>Project Management,</li>
      <li>Design,</li>
      <li>System Administration,</li>
      <li>Implementation,</li>
      <li>On-going Support</li>
      <li>and Cloud based Management Services</li>
    </ul>

    <address class="contact-block">
      <div class="street-address">418 Harbor Lane, Suite 210, Easton, MD 21601</div>
      <div class="phone">(555) 214-7790</div>
      <div class="web-address">www.redpinevector.net</div>
    </address>
  </section>
</body>
</html>
```